New LLC consulting company needs a business card design

I need a business card design for new company in Alexandria Virginia called TK Verdane Consulting LLC. The company is focused on consulting for defense and national security issues with expertise in nuclear and space topics. I would like to see designs that are simple and I am open to colors except for brown.

Target Market(s)

All businesses that are seeking consulting help

Industry/Entity Type

Consulting

Contact Information for Business Card

Name of company - TK Verdane Consulting LLC; name (Delia Hartwig) President; email: hartwigdl47@mailnest.example; Phone: 555-862-4197

Requirements
Must have
• The details described above
Nice to have
• I'm open to all ideas
Should not have
• No brown

```html
<!DOCTYPE html>
<html lang="en">
<head>
<meta charset="UTF-8">
<title>Delia Hartwig – TK Verdane Consulting LLC</title>
<link rel="stylesheet" href="https://fonts.googleapis.com/css2?family=Montserrat:wght@400;700&display=swap">
<style>
  :root {
    --page-bg: #1f1f1f;
    --card-bg: #ffffff;
    --accent: #1f3a5f;
    --text: #2b2b2b;
    --icon: #111111;
  }
  html, body {
    margin: 0;
    padding: 0;
    width: 1200px;
    height: 1059px;
    overflow: hidden;
    background: var(--page-bg);
  }
  .canvas {
    position: relative;
    width: 1200px;
    height: 1059px;
  }
  .business-card {
    position: absolute;
    left: 191px;
    top: 296px;
    width: 818px;
    height: 468px;
    background: var(--card-bg);
    border-radius: 24px;
    font-family: "Montserrat", sans-serif;
    overflow: hidden;
  }
  .company-name {
    position: absolute;
    left: 43px;
    top: 52px;
    margin: 0;
    display: flex;
    align-items: center;
    font-size: 22px;
    line-height: 1;
    font-weight: 700;
    color: var(--accent);
    letter-spacing: 0.3px;
  }
  .company-mark {
    width: 14px;
    height: 14px;
    margin-right: 12px;
    background: var(--accent);
    flex-shrink: 0;
  }
  .holder-name {
    position: absolute;
    right: 44px;
    top: 156px;
    margin: 0;
    font-size: 40px;
    line-height: 1;
    font-weight: 700;
    color: var(--accent);
    letter-spacing: -0.2px;
  }
  .holder-title {
    position: absolute;
    right: 44px;
    top: 208px;
    margin: 0;
    font-size: 21px;
    line-height: 1;
    font-weight: 400;
    color: var(--text);
    letter-spacing: 0.4px;
  }
  .divider {
    position: absolute;
    left: 43px;
    right: 43px;
    top: 255px;
    height: 2px;
    background: var(--accent);
  }
  .contact-list {
    position: absolute;
    left: 43px;
    top: 280px;
    margin: 0;
    padding: 0;
    list-style: none;
  }
  .contact-item {
    display: flex;
    align-items: center;
    height: 24px;
    margin-bottom: 14px;
    font-size: 20px;
    color: var(--text);
    letter-spacing: 0.3px;
  }
  .contact-icon {
    width: 19px;
    height: 19px;
    margin-right: 8px;
    flex-shrink: 0;
  }
</style>
</head>
<body>
<div class="canvas">
  <section class="business-card">
    <p class="company-name"><span class="company-mark"></span>TK Verdane Consulting LLC</p>
    <h1 class="holder-name">Delia Hartwig</h1>
    <p class="holder-title">President</p>
    <div class="divider"></div>
    <ul class="contact-list">
      <li class="contact-item">
        <svg class="contact-icon" viewBox="0 0 20 20" aria-hidden="true">
          <rect x="1" y="4" width="18" height="12" fill="var(--icon)"/>
          <path d="M1 4 L10 11 L19 4 M1 16 L8 9.5 M19 16 L12 9.5" stroke="#fff" stroke-width="1.3" fill="none"/>
        </svg>
        <span>hartwigdl47@mailnest.example</span>
      </li>
      <li class="contact-item">
        <svg class="contact-icon" viewBox="0 0 20 20" aria-hidden="true">
          <path d="M4.5 2 L7.5 5.5 L6 7.5 C7 10 9.5 12.5 12 13.5 L14 12 L17.5 15 L15.5 18 C9 17.5 2.5 11 2 4 Z" fill="var(--icon)"/>
          <path d="M11 2.5 A6.5 6.5 0 0 1 17.5 9 M11 5.5 A3.5 3.5 0 0 1 14.5 9" stroke="var(--icon)" stroke-width="1.6" fill="none"/>
        </svg>
        <span>555-862-4197</span>
      </li>
    </ul>
  </section>
</div>
</body>
</html>
```